依頼詳細
最終目的は会員入会ですが、まずは、8/16より開始する『内覧会、体験会』の
集客に焦点をあてた、女性が通ってみたいと思えるような、
折込ちらしをお願いします。

【全体で重視する点】
・一目でフィットネスのチラシがわかるように
・メインのモデル画像は女性(フィットネスらしさ重視)
・キャンペーン内容(8/16~9/30までの入会で9月.10月の月会費が0円)が
はっきりとわかるように、表現はお任せします。
・20~40代女性に向けた

※詳細な資料は、添付いたします。

ワークリンドのチラシ作成は初めての利用になり、
説明不足な点、追加事項等あるかと思いますが、よろしくお願いいたします。

記載項目
資料を添付します。
サイズ
B4
ページ数
両面
希望イメージ
• +5 0 +5
• シンプル
複雑
• 単色
カラフル
• 暗い
明るい
• 日常
高級
• 遊び心
厳粛
• 未来的
伝統的
• 女性的
男性的
希望する色
ロゴ色で使用している、オレンジ
納品ファイル
• 高解像度JPG (.jpg)
• イラストレーター形式 (.ai)
• フォトショップ形式 (.psd)
• PNG形式 (.png)
補足説明
依頼公開後の追記内容
ワークリンドの皆様

ご提案いただきありがとうございます。
弊社がイメージしている内容を追記させていただきます。

①メインとなる女性のイメージは、親しみやすい日本人の女性で
お願いします。イメージ画像添付します。(josei_imege)
②20代から40代の幅広い年齢層の集客を目指しているため
ちらしのどこかに30代もしくは40代女性の写真を入れてください。
③キャッチフレーズは、「カラダ引締めスタート」になります。
④HPのイメージ画像を添付します。
使用している画像の雰囲気を感じていただければ(hp_image)
⑤弊社に近いイメージのちらし「ミルヴァ」様を添付します。(MILVA)

追記点が多くなりましたが、引き続きよろしくお願いします。
ワークリンドの皆様

ご提案いただきありがとうございます。
残り時間わずかとなりますが、

①ちらしのどこかに、カタカナ表記「ルミエフィットネス」といれてください。
②和歌山初と入れている文言は、削除してください。
③ちらし表面に、「初心者オススメ」もしくは「初心者対象」といれてください。

```html
<!DOCTYPE html>
<html lang="ja">
<head>
<meta charset="utf-8">
<title>ルミエフィットネス 内覧会・体験会</title>
<link href="https://fonts.googleapis.com/css2?family=Noto+Sans+JP:wght@400;500;700;900&display=swap" rel="stylesheet">
<style>
:root{
  --orange:#f06a28;
  --orange-deep:#e0531a;
  --orange-soft:#fde3d3;
  --ink:#333333;
  --dark:#3a3634;
  --white:#ffffff;
  --cream:#fff7f1;
}
*{margin:0;padding:0;box-sizing:border-box}
html,body{width:844px;height:1200px;overflow:hidden;background:var(--white)}
body{font-family:"Noto Sans JP",sans-serif;color:var(--ink)}
ul{list-style:none}
.flyer{position:relative;width:844px;height:1200px;overflow:hidden}
.abs{position:absolute}

/* hero */
.hero-photo{left:0;top:0;width:844px;height:600px;
  background:linear-gradient(100deg,#4a4441 0%,#6d6560 35%,#b9aea6 60%,#d9cfc7 80%,#efe8e2 100%)}
.hero-tagline{left:30px;top:14px;font-size:13px;color:var(--white);font-weight:500;letter-spacing:.04em}
.hero-title{left:28px;top:62px;color:var(--white);font-weight:900;line-height:1.02}
.hero-title .line1{display:block;font-size:60px;color:#ffb08a;letter-spacing:.02em}
.hero-title .line2{display:block;font-size:72px;letter-spacing:.04em}

.reasons-head{left:24px;top:212px;color:var(--white);font-weight:900;font-size:22px}
.reasons-head b{color:#ffb08a;font-size:30px}
.reasons{left:22px;top:250px;width:420px;display:grid;grid-template-columns:repeat(3,134px);gap:9px}
.reason{height:88px;background:var(--orange);color:var(--white);text-align:center;
  display:flex;flex-direction:column;justify-content:center;padding:4px}
.reason small{font-size:10px;font-weight:500;color:#ffe0cc}
.reason strong{font-size:22px;font-weight:900;line-height:1.15;white-space:nowrap}
.reason strong.compact{font-size:18px;line-height:1.3}

.points-head{left:24px;top:450px;color:var(--white);font-weight:900;font-size:19px}
.points-head b{color:#ffb08a;font-size:24px}
.points{left:22px;top:484px;width:420px;display:grid;grid-template-columns:repeat(3,134px);gap:9px}
.point{height:62px;background:rgba(255,255,255,.95);text-align:center;position:relative;
  display:flex;align-items:center;justify-content:center;font-weight:700;font-size:14px;line-height:1.25;padding:14px 4px 4px}
.point i{position:absolute;top:-9px;left:50%;transform:translateX(-50%);background:var(--orange);color:var(--white);
  font-style:normal;font-size:11px;padding:1px 10px;border-radius:10px}
.option{left:22px;top:556px;width:420px;background:var(--white);display:flex;align-items:center;gap:8px;padding:4px 8px;font-size:11px}
.option .tag{color:var(--orange);font-weight:900;font-size:18px;line-height:1}
.option .tag small{display:block;font-size:8px;color:var(--ink);font-weight:500}

.badge{left:696px;top:480px;width:130px;height:130px;border-radius:50%;background:var(--white);
  border:4px solid var(--orange);color:var(--orange);font-weight:900;font-size:26px;line-height:1.15;
  display:flex;align-items:center;justify-content:center;text-align:center}

/* campaign */
.campaign{left:0;top:600px;width:844px;height:190px;background:var(--cream)}
.camp-photo{left:470px;top:608px;width:360px;height:176px;background:linear-gradient(135deg,#e9d9cc,#c9b6a8 60%,#a99688)}
.bubble{left:640px;top:614px;background:var(--white);border:2px solid var(--orange);border-radius:20px;
  font-size:12px;font-weight:700;padding:4px 12px;color:var(--ink)}
.camp-lead{left:20px;top:612px;font-size:13px;font-weight:700}
.camp-lead .now{color:var(--orange);font-size:17px}
.camp-title{left:20px;top:636px;background:var(--orange);color:var(--white);font-weight:900;font-size:27px;padding:2px 14px;line-height:1.4}
.camp-line{left:20px;font-size:22px;font-weight:900;line-height:1;white-space:nowrap}
.camp-line.fee{top:684px}
.camp-line.entry{top:722px}
.camp-line s{color:#888;font-weight:700}
.camp-line .zero{color:var(--orange);font-size:40px}
.camp-line small{font-size:10px;font-weight:500}
.camp-extra{left:20px;top:752px;font-size:22px;font-weight:900;color:var(--orange);line-height:1.2}
.camp-extra span{color:var(--ink);font-size:15px;margin-right:6px}

/* info */
.info{left:0;top:790px;width:430px;height:410px;background:var(--white)}
.brand{left:22px;top:800px;font-size:22px;font-weight:900;color:var(--orange);display:flex;align-items:center;gap:8px}
.brand::before{content:"";width:14px;height:14px;background:var(--orange)}
.address{left:22px;top:834px;font-size:11px}
.tel{left:22px;top:850px;font-size:34px;font-weight:900;color:var(--orange);display:flex;align-items:center;gap:6px}
.web{left:22px;top:898px;font-size:11px;font-weight:500}
.hours{left:22px;top:918px;width:396px;border-collapse:collapse;font-size:11px}
.hours th{background:var(--orange);color:var(--white);font-weight:700;padding:3px 6px;text-align:left}
.hours td{border-bottom:1px solid #ddd;padding:3px 6px}
.map{left:22px;top:990px;width:396px;height:196px;background:#eeeeee;border:1px solid #ccc}
.map-label{left:40px;top:1080px;font-size:18px;font-weight:700;color:#777}

.visit-photo{left:430px;top:790px;width:414px;height:410px;background:linear-gradient(160deg,#f1e9e1,#d8c6b7 55%,#b9a494)}
.visit-bubble{left:620px;top:812px;width:190px;height:70px;background:var(--white);border-radius:50%;
  display:flex;align-items:center;justify-content:center;text-align:center;font-size:14px;font-weight:700;line-height:1.3}
.visit-title{left:446px;top:1062px;font-size:50px;font-weight:900;color:var(--orange);letter-spacing:.02em;line-height:1.2;white-space:nowrap;
  text-shadow:0 0 6px var(--white),0 0 6px var(--white)}
.visit-date{left:586px;top:1136px;background:var(--orange);color:var(--white);font-weight:900;font-size:28px;line-height:1.4;padding:2px 16px;white-space:nowrap}
</style>
</head>
<body>
<main class="flyer">
  <div class="abs hero-photo" role="img" aria-label="イヤホンをつけてトレーニングする女性の写真"></div>
  <p class="abs hero-tagline">もっと健康に、ダイエットしたい、そう思っている方にぴったりのお知らせです</p>
  <h1 class="abs hero-title"><span class="line1">カラダ引締め</span><span class="line2">スタート</span></h1>

  <h2 class="abs reasons-head">ルミエフィットネスを選ぶ<b>6</b>つの理由</h2>
  <ul class="abs reasons">
    <li class="reason"><small>オリエン無料完備で</small><strong>初心者に<br>優しい</strong></li>
    <li class="reason"><small>月会費5,980円で</small><strong>嬉しい<br>料金設定</strong></li>
    <li class="reason"><small>いつでも好きな時間に</small><strong>24時間<br>年中無休</strong></li>
    <li class="reason"><small>60台の</small><strong>最新鋭<br>マシン</strong></li>
    <li class="reason"><small>高速無線もOK</small><strong>Wifi<br>使い放題</strong></li>
    <li class="reason"><small>静脈認証入退で</small><strong class="compact">セキュリティ<br>万全</strong></li>
  </ul>

  <h2 class="abs points-head">女性に嬉しい<b>3</b>つのポイント</h2>
  <ul class="abs points">
    <li class="point"><i>清潔</i>シャワールーム、<br>更衣室完備</li>
    <li class="point"><i>快適</i>フリートレーニング<br>エリアあり</li>
    <li class="point"><i>充実</i>ストレッチ<br>ゾーン完備</li>
  </ul>
  <div class="abs option">
    <span class="tag"><small>もっと便利にする</small>オプション</span>
    <span>[水素水] 500円/月 飲み放題<br>[個人用置き場ロッカー] 1000円/月</span>
  </div>
  <div class="abs badge">初心者<br>対象</div>

  <section class="abs campaign"></section>
  <div class="abs camp-photo" role="img" aria-label="ストレッチをする女性たちの写真"></div>
  <p class="abs bubble">お気軽にご相談ください</p>
  <p class="abs camp-lead"><span class="now">今だけ</span> 8/16(木)〜9/12(水)にご入会のお客様のみ</p>
  <h2 class="abs camp-title">期間限定キャンペーン実施中</h2>
  <p class="abs camp-line fee">[月会費] <s>5,980円</s>×2ヶ月→<span class="zero">0</span>円</p>
  <p class="abs camp-line entry">[入会金] 3,000円 <small>[登録手数料込]</small> → 2,000円</p>
  <p class="abs camp-extra"><span>さらに!</span>水素水2ヶ月無料</p>

  <section class="abs info"></section>
  <p class="abs brand">LUMIEFITNESS24</p>
  <p class="abs address">〒640-0000 和歌山県和歌山市南町1-2-3 ルミエビル1F</p>
  <p class="abs tel"><svg width="30" height="30" viewBox="0 0 24 24" aria-hidden="true"><path fill="#f06a28" d="M6.6 10.8a15.1 15.1 0 0 0 6.6 6.6l2.2-2.2a1 1 0 0 1 1-.25 11.4 11.4 0 0 0 3.6.57 1 1 0 0 1 1 1V20a1 1 0 0 1-1 1A17 17 0 0 1 3 4a1 1 0 0 1 1-1h3.5a1 1 0 0 1 1 1c0 1.25.2 2.45.57 3.57a1 1 0 0 1-.25 1z"/></svg>073-555-0148</p>
  <p class="abs web">ご利用時間 24時間年中無休　lumie-fitness.example</p>
  <table class="abs hours">
    <tr><th colspan="2">スタッフ常駐時間</th></tr>
    <tr><td>月〜金</td><td>10:00〜21:00</td></tr>
    <tr><td>土・日・祝</td><td>10:00〜18:00</td></tr>
  </table>
  <div class="abs map" role="img" aria-label="店舗周辺の地図"></div>
  <p class="abs map-label">地図</p>

  <div class="abs visit-photo" role="img" aria-label="笑顔でくつろぐ女性の写真"></div>
  <p class="abs visit-bubble">まずは雰囲気を<br>見に来てください</p>
  <h2 class="abs visit-title">内覧会・体験会</h2>
  <p class="abs visit-date">8.16(木)スタート</p>
</main>
</body>
</html>
```